India Export Business Card Design

We are a small company importing from India,
Antique furniture and textiles.
We would like a design with somthing of India in it.
IE: Camels, Tuk Tuks, People or maybe Taj Mahal.
Only one of the above suggestions, we do not want the card to be to busy.
We travel to India twice a year to get the product and then come home to New Zealand and sell it.
And must have our business name which is
Kestrel Trading Company
Nz phone no. 64 9 375 8162
Mobile 64 21 603 174
Email briony@kestreltrading.co.nz
Www.kestreltrading.co.nz

Also my name and position
Briony Calder
Director

Reason: I am awaiting for a design to come back with different colours. Many thanks

Target Market(s)

Indian heritage furniture and textiles in India also
New Zealand market for public to buy the goods that is bought in India

Industry/Entity Type

Travel

Contact Information for Business Card

Kestrel Trading Company
17b Orland Road
RD 5 Papakura 2417
Auckland
New Zealand
email address which will be associated to our new website
website once we have it assigned

Requirements
Must have
• Company name and region.
Phone numbers
My name and title.
Nice to have
• I would like the card to portray India and as i said before, I like the idea of camels in a line with ropes between them like an animation.
But happy to see what other suggestions there are.

```html
<!DOCTYPE html>
<html lang="en">
<head>
<meta charset="utf-8">
<title>Kestrel Trading Company – Business Cards</title>
<link rel="stylesheet" href="https://fonts.googleapis.com/css2?family=Courgette&family=Kaushan+Script&family=Questrial&display=swap">
<style>
  :root {
    --backdrop: #a7a7a7;
    --card: #ffffff;
    --crimson: #b5122f;
    --maroon: #6e1426;
    --tone-pink: #e77ab0;
    --tone-blue: #6cc6e6;
    --tone-gold: #f4d65a;
  }
  * { box-sizing: border-box; margin: 0; padding: 0; }
  html, body {
    width: 1200px;
    height: 899px;
    overflow: hidden;
    background: var(--backdrop);
  }
  .canvas {
    position: relative;
    width: 1200px;
    height: 899px;
  }
  .card {
    position: absolute;
    left: 270px;
    width: 660px;
    height: 378px;
    background: var(--card);
    overflow: hidden;
    box-shadow: 0 3px 10px rgba(0,0,0,0.18);
  }
  .card--company { top: 52px; }
  .card--personal { top: 470px; }

  .ornament-area {
    position: absolute;
    border-radius: 50%;
    background: linear-gradient(135deg, var(--tone-gold) 0%, var(--tone-pink) 50%, var(--tone-blue) 100%);
  }
  .card--company .ornament-area { width: 300px; height: 300px; left: -100px; top: 32px; }
  .card--personal .ornament-area { width: 270px; height: 270px; left: -40px; top: 4px; }

  .company-block {
    position: absolute;
    left: 240px;
    top: 76px;
    width: 400px;
    text-align: center;
    color: var(--maroon);
    font-family: "Questrial", sans-serif;
  }
  .company-name {
    font-family: "Courgette", cursive;
    color: var(--crimson);
    font-size: 30px;
    font-weight: 400;
    white-space: nowrap;
    margin-bottom: 6px;
  }
  .company-web,
  .company-phone {
    font-size: 22px;
    line-height: 1.15;
    letter-spacing: 0.6px;
  }

  .person-name {
    position: absolute;
    left: 262px;
    top: 88px;
    font-family: "Kaushan Script", cursive;
    color: var(--crimson);
    font-size: 56px;
    font-weight: 400;
    white-space: nowrap;
  }
  .person-title {
    position: absolute;
    left: 372px;
    top: 166px;
    font-family: "Questrial", sans-serif;
    color: var(--maroon);
    font-size: 30px;
  }
  .person-contact {
    position: absolute;
    left: 246px;
    top: 258px;
    font-family: "Questrial", sans-serif;
    color: var(--maroon);
    font-size: 20px;
    line-height: 1.2;
    list-style: none;
  }
  .person-contact .mobile { padding-left: 52px; }
</style>
</head>
<body>
<main class="canvas">
  <section class="card card--company">
    <div class="ornament-area" role="img" aria-label="Colourful Indian mandala ornament in pink, blue, yellow and maroon"></div>
    <div class="company-block">
      <h1 class="company-name">Kestrel Trading Company</h1>
      <p class="company-web">kestreltrading.co.nz</p>
      <p class="company-phone">64 9 375 8162</p>
    </div>
  </section>

  <section class="card card--personal">
    <div class="ornament-area" role="img" aria-label="Colourful Indian mandala ornament in pink, blue, yellow and maroon"></div>
    <h2 class="person-name">Briony Calder</h2>
    <p class="person-title">Director</p>
    <ul class="person-contact">
      <li class="mobile">64 21 603 174</li>
      <li class="email">briony@kestreltrading.co.nz</li>
    </ul>
  </section>
</main>
</body>
</html>
```